Tide Harbor Finance Business Cards

Looking for a business card for a new mortgage broking business. Name of the business is Tide Harbor Finance. Purpose of the business is to build trust and strong relationships with clients to then assist them with your mortgage lending needs. Most relationships within the business start off as an enquiry, and then can evolve into a 10+ year relationship, servicing clients from purchasing a new home to then upgrading for their family and even then assisting their children with their first home purchase. Business card should communicate financial security and trust.

Target Market(s)

Targeting professional clients who are looking to build a relationship with a knowledgeable mortgage professional

Industry/Entity Type

Finance - Home Loans

Contact Information for Business Card

Peter Colburn, Director, mobile: 0427 903186, email:peter@tideharborfinance.com.au, website: www.tideharborfinance.com.au

Font styles to use
Sans Serif

Requirements
Must have
• On the front: Must have company logo, contact details as above. On the back: slogan, 'Clear choices, calm decisions', plus listing services offered: home loans, investment loans, first home buyers, refinancing, car finance

```html
<!DOCTYPE html>
<html lang="en">
<head>
<meta charset="utf-8">
<title>Tide Harbor Finance Business Cards</title>
<link rel="stylesheet" href="https://fonts.googleapis.com/css2?family=Montserrat:wght@400;500;700;800&display=swap">
<style>
  :root {
    --navy: #0d4f7c;
    --orange: #f2a11f;
    --white: #ffffff;
    --ink: #1f2d3a;
    --backdrop: #e6e8eb;
  }
  * { margin: 0; padding: 0; box-sizing: border-box; }
  html, body { width: 1200px; height: 874px; overflow: hidden; }
  body {
    background: var(--backdrop);
    font-family: "Montserrat", sans-serif;
    position: relative;
  }
  .card {
    position: absolute;
    width: 620px;
    height: 354px;
    background: var(--white);
    border-radius: 18px;
    overflow: hidden;
    box-shadow: 0 10px 30px rgba(0,0,0,0.18);
  }

  /* Back card */
  .card-back { left: 460px; top: 48px; }
  .slogan {
    position: absolute;
    top: 34px; left: 0; right: 0;
    text-align: center;
    color: var(--orange);
    font-weight: 700;
    font-size: 19px;
    letter-spacing: 0.3px;
  }
  .brand-name {
    font-family: "Montserrat", sans-serif;
    font-weight: 800;
    color: var(--navy);
    text-transform: uppercase;
    line-height: 0.95;
  }
  .card-back .brand-name {
    position: absolute;
    left: 0; right: 0; top: 90px;
    text-align: center;
    font-size: 58px;
  }
  .services-band {
    position: absolute;
    left: 0; right: 0; bottom: 0;
    height: 40px;
    background: var(--navy);
    color: var(--white);
    font-size: 14px;
    display: flex;
    align-items: center;
    justify-content: center;
    gap: 9px;
  }
  .services-band .dot {
    width: 7px; height: 7px;
    border-radius: 50%;
    background: var(--orange);
  }

  /* Front card */
  .card-front { left: 120px; top: 470px; }
  .card-front .brand-name {
    position: absolute;
    left: 36px; top: 96px;
    width: 230px;
    font-size: 38px;
  }
  .divider {
    position: absolute;
    left: 282px; top: 70px;
    width: 2px; height: 150px;
    background: var(--navy);
  }
  .contact-block {
    position: absolute;
    left: 304px; top: 72px;
  }
  .person-name {
    color: var(--navy);
    font-weight: 800;
    font-size: 27px;
    letter-spacing: 0.5px;
  }
  .person-title {
    color: var(--ink);
    font-size: 15px;
    margin-top: 2px;
    margin-bottom: 16px;
  }
  .contact-line {
    display: flex;
    align-items: center;
    gap: 9px;
    color: var(--ink);
    font-size: 15px;
    margin-bottom: 7px;
  }
  .contact-line svg { width: 15px; height: 15px; flex: none; }
  .swoosh {
    position: absolute;
    left: 0; bottom: 0;
    width: 620px; height: 120px;
  }
</style>
</head>
<body>

  <section class="card card-back" aria-label="Card back">
    <p class="slogan">Clear choices, calm decisions</p>
    <p class="brand-name">Tide<br>Harbor<br>Finance</p>
    <div class="services-band">
      <span>Home loans</span><span class="dot"></span>
      <span>Investment loans</span><span class="dot"></span>
      <span>First home buyers</span><span class="dot"></span>
      <span>Refinancing</span><span class="dot"></span>
      <span>Car finance</span>
    </div>
  </section>

  <section class="card card-front" aria-label="Card front">
    <p class="brand-name">Tide<br>Harbor<br>Finance</p>
    <div class="divider"></div>
    <div class="contact-block">
      <p class="person-name">Peter Colburn</p>
      <p class="person-title">Director</p>
      <p class="contact-line">
        <svg viewBox="0 0 16 16"><rect x="4" y="1" width="8" height="14" rx="1.5" fill="none" stroke="var(--orange)" stroke-width="1.6"/><circle cx="8" cy="12.5" r="0.9" fill="var(--orange)"/></svg>
        0427 903186
      </p>
      <p class="contact-line">
        <svg viewBox="0 0 16 16"><rect x="1" y="3.5" width="14" height="9" fill="var(--navy)"/><path d="M1 3.5 L8 9 L15 3.5" fill="none" stroke="var(--white)" stroke-width="1.2"/></svg>
        peter@tideharborfinance.com.au
      </p>
      <p class="contact-line">
        <svg viewBox="0 0 16 16"><circle cx="8" cy="8" r="6.5" fill="var(--navy)"/><path d="M1.5 8 H14.5 M8 1.5 C5 5 5 11 8 14.5 M8 1.5 C11 5 11 11 8 14.5" fill="none" stroke="var(--white)" stroke-width="0.9"/></svg>
        www.tideharborfinance.com.au
      </p>
    </div>
    <svg class="swoosh" viewBox="0 0 620 120" preserveAspectRatio="none" aria-hidden="true">
      <path d="M0 0 C150 60 380 88 620 84 L620 120 L0 120 Z" fill="var(--orange)"/>
      <path d="M0 8 C150 68 380 96 620 94 L620 120 L0 120 Z" fill="var(--white)"/>
      <path d="M0 16 C150 76 380 104 620 104 L620 120 L0 120 Z" fill="var(--navy)"/>
      <path d="M0 50 L0 120 L80 120 C50 100 20 80 0 50 Z" fill="var(--navy)"/>
    </svg>
  </section>

</body>
</html>
```